Fernvale Pharmacy opening

We want to have a double sided 5.5"x8.5" flyer for a new Pharmacy opening in a well known strip mall in the neighborhood and we are planning to mail it to neighbors homes.

Want to put the outside pharmacy picture on the main side of the flyer and a coupon with 25% off towards an OTC product on the back in addition to the info below (preferably in a sort of bulletin points not a list (something like the 2 examples attached).

Colors to be red like the exterior sign and blue like the interior wall paint:

Front side should have:
Fernvale pharmacy
Your locally owned and operated pharmacy around the corner.
317-4082 Tarrow rd.
Brisket hollow plaza
T. 604 827 5530 (call or text)
F. 604-827-5532

Free prescription delivery
Text us for refills
Specialized compounding
Customized compression stockings

The back side should have:

Do you forget taking your medications! We offer multiple compliance packaging options at no additional cost.
Had shingles before or worried to have it? travelling soon? check our vaccinations options!
Suffering side effects? We are experienced to check your medications interactions & different coverage options.
Hard time monitoring your blood pressure? Trying to stop smoking? we can always help.

FEELING BETTER STARTS HERE

```html
<!DOCTYPE html>
<html lang="en">
<head>
<meta charset="utf-8">
<title>Fernvale Pharmacy – Flyer</title>
<link rel="stylesheet" href="https://fonts.googleapis.com/css2?family=Bebas+Neue&family=Hind:wght@500;600;700&family=Exo+2:ital,wght@0,700;0,800;1,700;1,800&family=Kalam:wght@400&display=swap">
<style>
  :root {
    --navy: #2c3a5b;
    --red: #e3171f;
    --white: #ffffff;
    --page: #e9eaec;
    --photo-a: #e8432c;
    --photo-b: #c9201c;
    --shelf-a: #f3e6df;
    --shelf-b: #ffffff;
  }
  * { margin: 0; padding: 0; box-sizing: border-box; }
  html, body { width: 1200px; height: 923px; overflow: hidden; background: var(--page); }
  .canvas { position: relative; width: 1200px; height: 923px; }
  .flyer {
    position: absolute; top: 101px; width: 468px; height: 722px;
    background: var(--white); overflow: hidden;
  }
  .flyer--front { left: 118px; }
  .flyer--back { left: 614px; }
  .shape { position: absolute; left: 0; top: 0; }

  /* front */
  .front-title {
    position: absolute; left: 0; width: 100%; top: 18px; text-align: center;
    font-family: "Bebas Neue", sans-serif; font-size: 58px; line-height: 58px;
    color: var(--white); letter-spacing: 0.5px;
  }
  .storefront-photo {
    position: absolute; left: 0; top: 91px; width: 468px; height: 295px;
    background: linear-gradient(160deg, var(--photo-a) 0%, var(--photo-b) 100%);
    clip-path: polygon(0 22px, 233px 0, 468px 20px, 468px 295px, 0 295px);
  }
  .tagline {
    position: absolute; left: 0; width: 100%; top: 403px; text-align: center;
    font-family: "Hind", sans-serif; font-weight: 700; font-size: 35px; line-height: 36px;
    color: var(--white);
  }
  .services {
    position: absolute; left: 53px; top: 540px; list-style: none;
    font-family: "Hind", sans-serif; font-weight: 700; font-size: 19.5px; line-height: 23px;
    color: var(--red);
  }
  .services li { display: flex; align-items: center; gap: 8px; }
  .services svg { width: 20px; height: 20px; flex: none; }
  .contact {
    position: absolute; left: 0; width: 100%; top: 662px; text-align: center;
    font-family: "Hind", sans-serif; font-weight: 600; font-size: 16px; line-height: 23px;
    color: var(--white);
  }
  .contact svg { width: 14px; height: 17px; vertical-align: -3px; }

  /* back */
  .shelves-photo {
    position: absolute; left: 0; top: 91px; width: 468px; height: 520px;
    background: linear-gradient(180deg, var(--shelf-a) 0%, var(--shelf-a) 55%, var(--shelf-b) 100%);
  }
  .back-title {
    position: absolute; left: 0; width: 100%; top: 22px; text-align: center;
    font-family: "Exo 2", sans-serif; font-weight: 800; font-size: 29px; line-height: 31px;
    color: var(--white); letter-spacing: 0.5px;
  }
  .offer, .expertise {
    position: absolute; left: 0; width: 100%; text-align: center;
    font-family: "Exo 2", sans-serif; font-weight: 700; font-style: italic; color: var(--red);
  }
  .offer { top: 112px; font-size: 21px; line-height: 26px; }
  .expertise { top: 578px; font-size: 18px; line-height: 24px; }
  .questions {
    position: absolute; left: 84px; top: 0; list-style: none;
    font-family: "Hind", sans-serif; font-weight: 600; font-size: 25.5px; line-height: 26.5px;
    color: var(--navy);
  }
  .questions li { position: absolute; left: 0; width: 340px; padding-left: 31px; }
  .questions svg { position: absolute; left: 0; top: 3px; width: 32px; height: 30px; }
  .signoff {
    position: absolute; left: 0; width: 100%; top: 662px; text-align: center;
    font-family: "Kalam", cursive; font-size: 28px; line-height: 34px; color: var(--white);
  }
</style>
</head>
<body>
<div class="canvas">

  <section class="flyer flyer--front">
    <svg class="shape" width="468" height="722" aria-hidden="true">
      <rect x="0" y="0" width="468" height="120" fill="var(--navy)"/>
      <rect x="0" y="386" width="468" height="136" fill="var(--navy)"/>
      <rect x="0" y="650" width="468" height="72" fill="var(--navy)"/>
    </svg>
    <h1 class="front-title">FERNVALE PHARMACY</h1>
    <div class="storefront-photo" role="img" aria-label="Photo of the pharmacy storefront with its red exterior sign in the strip mall"></div>
    <p class="tagline">Your Locally Owned<br>And Operated Pharmacy<br>Around The Corner.</p>
    <ul class="services">
      <li><svg viewBox="0 0 20 20"><circle cx="9.5" cy="10.5" r="7.5" fill="none" stroke="var(--navy)" stroke-width="1.8"/><path d="M5.5 10.5l3 3 8-9" fill="none" stroke="var(--navy)" stroke-width="2.2"/></svg>FREE prescription delivery</li>
      <li><svg viewBox="0 0 20 20"><circle cx="9.5" cy="10.5" r="7.5" fill="none" stroke="var(--navy)" stroke-width="1.8"/><path d="M5.5 10.5l3 3 8-9" fill="none" stroke="var(--navy)" stroke-width="2.2"/></svg>SPECIALIZED compounding</li>
      <li><svg viewBox="0 0 20 20"><circle cx="9.5" cy="10.5" r="7.5" fill="none" stroke="var(--navy)" stroke-width="1.8"/><path d="M5.5 10.5l3 3 8-9" fill="none" stroke="var(--navy)" stroke-width="2.2"/></svg>TEXT US for refills</li>
      <li><svg viewBox="0 0 20 20"><circle cx="9.5" cy="10.5" r="7.5" fill="none" stroke="var(--navy)" stroke-width="1.8"/><path d="M5.5 10.5l3 3 8-9" fill="none" stroke="var(--navy)" stroke-width="2.2"/></svg>CUSTOMIZED compression stockings</li>
    </ul>
    <p class="contact">317-4082 Tarrow rd. Brisket hollow plaza<br>(Call or Text)
      <svg viewBox="0 0 14 17"><rect x="2" y="1" width="10" height="15" rx="1.5" fill="none" stroke="var(--white)" stroke-width="1.5"/><line x1="5.5" y1="13.5" x2="8.5" y2="13.5" stroke="var(--white)" stroke-width="1.2"/></svg>604 827 5530
      <svg viewBox="0 0 16 17" style="width:16px"><rect x="4" y="1" width="8" height="5" fill="none" stroke="var(--white)" stroke-width="1.4"/><rect x="1" y="6" width="14" height="7" rx="1" fill="var(--white)"/><rect x="4" y="11" width="8" height="5" fill="var(--navy)" stroke="var(--white)" stroke-width="1.2"/></svg>604-827-5532</p>
  </section>

  <section class="flyer flyer--back">
    <div class="shelves-photo" role="img" aria-label="Faded photo of pharmacy shelves stocked with products"></div>
    <svg class="shape" width="468" height="722" aria-hidden="true">
      <polygon points="0,0 468,0 468,112 234,91 0,112" fill="var(--navy)"/>
      <rect x="0" y="650" width="468" height="72" fill="var(--navy)"/>
      <path d="M173 701 C 240 692, 330 688, 372 695" fill="none" stroke="var(--red)" stroke-width="2.5" stroke-linecap="round"/>
    </svg>
    <h2 class="back-title">DO YOU FORGET TAKING<br>YOUR MEDICATIONS!</h2>
    <p class="offer">We Offer Multiple<br>Compliance Packaging Options<br>At No Additional Cost.</p>
    <ul class="questions">
      <li style="top:218px"><svg viewBox="0 0 32 30"><circle cx="14" cy="16" r="11.5" fill="none" stroke="var(--red)" stroke-width="2.4"/><path d="M7 15l6 6 16-18" fill="none" stroke="var(--red)" stroke-width="3.4" stroke-linecap="round"/></svg>Had shingles before or worried to have it?</li>
      <li style="top:282px"><svg viewBox="0 0 32 30"><circle cx="14" cy="16" r="11.5" fill="none" stroke="var(--red)" stroke-width="2.4"/><path d="M7 15l6 6 16-18" fill="none" stroke="var(--red)" stroke-width="3.4" stroke-linecap="round"/></svg>Travelling soon?</li>
      <li style="top:318px"><svg viewBox="0 0 32 30"><circle cx="14" cy="16" r="11.5" fill="none" stroke="var(--red)" stroke-width="2.4"/><path d="M7 15l6 6 16-18" fill="none" stroke="var(--red)" stroke-width="3.4" stroke-linecap="round"/></svg>check our vaccinations options!</li>
      <li style="top:381px"><svg viewBox="0 0 32 30"><circle cx="14" cy="16" r="11.5" fill="none" stroke="var(--red)" stroke-width="2.4"/><path d="M7 15l6 6 16-18" fill="none" stroke="var(--red)" stroke-width="3.4" stroke-linecap="round"/></svg>Suffering side effects?</li>
      <li style="top:418px"><svg viewBox="0 0 32 30"><circle cx="14" cy="16" r="11.5" fill="none" stroke="var(--red)" stroke-width="2.4"/><path d="M7 15l6 6 16-18" fill="none" stroke="var(--red)" stroke-width="3.4" stroke-linecap="round"/></svg>Hard time monitoring your blood pressure?</li>
      <li style="top:481px"><svg viewBox="0 0 32 30"><circle cx="14" cy="16" r="11.5" fill="none" stroke="var(--red)" stroke-width="2.4"/><path d="M7 15l6 6 16-18" fill="none" stroke="var(--red)" stroke-width="3.4" stroke-linecap="round"/></svg>Trying to stop smoking?</li>
      <li style="top:528px"><svg viewBox="0 0 32 30"><circle cx="14" cy="16" r="11.5" fill="none" stroke="var(--red)" stroke-width="2.4"/><path d="M7 15l6 6 16-18" fill="none" stroke="var(--red)" stroke-width="3.4" stroke-linecap="round"/></svg>We can always help.</li>
    </ul>
    <p class="expertise">We are experienced to check your medications<br>interactions &amp; different coverage options.</p>
    <p class="signoff">Feeling Better Starts Here</p>
  </section>

</div>
</body>
</html>
```